Website Design Brief – B2B Industrial Engineering Company

DO NOT CONTACT ME PRIVATELY. ANY INQUIRES WILL BE IGNORED.

1. Industry & Company Background

We are a Swiss B2B engineering and manufacturing company operating in the fields of:
• Industrial air technology (Lufttechnik)
• Metal fabrication and plant construction (Metallbau / Anlagebau)
• Design, fabrication, installation, maintenance, and servicing of:
• Spray booths / paint booths
• Extraction and ventilation systems
• Filtration and environmentally efficient air-handling systems

We plan, build, manufacture, sell, install, and maintain these systems.
Most systems are custom-built in-house (metalwork, apparatus construction, air technology), tailored to customer requirements rather than relying only on standard components.

We are a family-run business with a strong focus on:
• Swiss quality
• Long-term experience
• Reliability and engineering competence
• Environmental efficiency
• Apprenticeship training (we train apprentices in our workshop)

2. Goal of the New Website

The new website should be a modernized evolution of our existing site, not a complete reinvention.

Key objectives:
• Look more modern, fresh, and dynamic
• Clearly communicate our experience, quality, and values
• Emphasize Swiss engineering, tradition, and reliability
• Feel professional and trustworthy, not flashy
• Be clean, uncluttered, and highly structured
• Encourage visitors to submit an inquiry or contact us

The website should feel confident and industrial-premium, with a strong focus on clarity and usability.

3. Overall Design Direction

Visual Style
• Modern industrial design
• Clean layouts with strong structure
• Clear visual hierarchy
• Balanced use of whitespace
• Calm, confident, engineering-focused look

Layout Principles (Important)
• Use clearly separated sections
• Avoid overlapping elements
• Avoid overly complex or experimental layouts
• Prefer grid-based, structured compositions
• Each section should have a clear start and end
• Designs should translate well into standard web layouts without reliance on floating or layered effects

Motion & Media
• A video header on the homepage is strongly desired
• Industrial footage, workshop, fabrication, systems in operation, or environmental technology
• Subtle animations are welcome (e.g., fades, simple transitions)
• Avoid heavy parallax or effects that depend on overlapping elements

4. Target Audience
• Industrial and B2B clients
• Engineers, facility managers, workshop owners
• Decision-makers looking for reliable long-term partners
• Customers who value custom solutions, quality, and service

5. Reference Website

Existing website (content & structure reference):
https://www.glanzhallenwerk.ch

This site:
• Provides existing branding, colors, and tone
• Is the baseline for content and structure
• Should be visually improved, simplified, and modernized

6. Pages to Design (Initial Phase – 5 Pages)

Please design 5 key pages, based on the existing website structure:
1. Home
• Video header
• Clear value proposition
• Overview of services
• Trust elements (experience, Swiss quality, family business)
• Strong call-to-action (Contact / Request Quote)
2. Company / About Us
• Company history
• Values and philosophy
• Swiss quality and tradition
• Family business
• Apprenticeship training and workshop
3. Services / Solutions
• Planning
• Manufacturing
• Installation
• Maintenance & service
• Custom systems vs standard components
4. Products / Systems
• Spray booths
• Extraction systems
• Filtration and air technology
• Modular but clearly structured sections
5. Contact
• Contact form
• Company details
• Location
• Clear inquiry-focused layout

7. Functional Requirements

Must Have
• Contact form
• Newsletter signup
• Cookie consent (EU / GDPR compliant)
• Privacy policy and legal pages (EU data protection)
• Clear navigation structure
• PDF catalog download area (well organized)

Must NOT Have
• No search feature
• No cluttered mega-menus
• No hidden or confusing navigation

8. Future Expansion (Phase Two – Not Required Now)

Designs should allow future expansion, including:
• Multi-language support (English, French, Italian)
• Optional webshop integration
• Expanded product catalog
• Additional service pages

These features do not need to be designed now, but the layout should be flexible enough to support them later.

9. Colors & Branding
• Use colors similar to the existing website
• Industrial, neutral tones preferred
• Accents should feel technical and professional
• Avoid trendy or overly bright color palettes

10. Tone & Messaging

The design should communicate:
• Experience
• Precision
• Trust
• Environmental responsibility
• Custom engineering capability
• Long-term partnership mindset

The overall impression should be:

“A modern Swiss engineering company with deep experience, strong values, and reliable solutions.”

11. Final Notes for Designers
• Focus on clarity, structure, and usability
• Designs should be realistic to implement with standard web layouts
• Avoid designs that rely on overlapping elements or complex layering
• Think in terms of clean sections, strong grids, and clear content flow
• The primary conversion goal is customer inquiries

Target Market(s)

The target market is B2B industrial customers, not consumers.

Industry/Entity Type

B2B industrial engineering and manufacturing (air technology, metal construction, plant engineering).

Number of Pages Required

5+ page

Requirements
Must have
• Clean structured layout, clear B2B positioning, video header, strong inquiry CTA, contact form, GDPR compliance, PDF downloads.
Nice to have
• Newsletter signup, multilingual-ready structure, future webshop support.
Should not have
• Search feature, overlapping elements, complex layered layouts, cluttered navigation.

```html
<!DOCTYPE html>
<html lang="en">
<head>
<meta charset="utf-8">
<title>Glanzhallen – Contact</title>
<link href="https://fonts.googleapis.com/css2?family=Inter:wght@400;500;600;700;800&display=swap" rel="stylesheet">
<style>
:root{
  --red:#ee2416;
  --red-soft:#fde6e4;
  --ink:#111111;
  --text:#2a2a2a;
  --muted:#555;
  --line:#e2e2e2;
  --page:#ffffff;
  --light:#f7f7f7;
  --dark:#121212;
  --dark2:#2e2e2e;
}
*{box-sizing:border-box;margin:0;padding:0}
html,body{width:1200px;height:2402px;overflow:hidden}
body{font-family:'Inter',Arial,sans-serif;color:var(--text);background:var(--page);position:relative}
.brand{display:flex;align-items:center;gap:9px;font-weight:700;font-size:12px;letter-spacing:.06em;color:#fff}
.brand-mark{width:22px;height:22px;border-radius:5px;background:var(--red);color:#fff;font-size:9px;display:flex;align-items:center;justify-content:center;font-weight:700;letter-spacing:0}
.btn{background:var(--red);color:#fff;font-weight:600;border-radius:3px;display:inline-flex;align-items:center;justify-content:center}

/* hero */
.hero{height:309px;background:radial-gradient(ellipse 180px 160px at 120px 190px,rgba(110,20,15,.45),transparent),radial-gradient(ellipse 200px 180px at 1110px 150px,rgba(110,20,15,.4),transparent),#121212;position:relative;color:#fff}
.nav{position:absolute;top:0;left:220px;width:759px;height:40px;display:flex;align-items:center;justify-content:space-between}
.nav-links{display:flex;align-items:center;gap:23px;font-size:10px;color:#e8e8e8}
.nav-links .btn{padding:0 15px;height:27px;font-size:10.5px;margin-left:0}
.hero-body{position:absolute;left:340px;top:110px}
.tag{display:inline-flex;align-items:center;gap:7px;height:25px;padding:0 11px;border:1px solid #3a3a3a;background:#2a2a2a;border-radius:13px;font-size:8.5px;font-weight:600;letter-spacing:.03em}
.tag::before{content:"";width:4px;height:4px;border-radius:50%;background:var(--red)}
.hero h1{font-size:38px;font-weight:700;letter-spacing:-.01em;margin-top:14px;line-height:1.1}
.hero p{font-size:11px;line-height:1.6;margin-top:18px;width:400px;color:#e6e6e6}

/* contact */
.contact{height:576px;position:relative}
.info{position:absolute;left:260px;top:60px;width:200px}
.info h2{font-size:15px;font-weight:600;color:var(--ink);margin-bottom:22px}
.info-item{display:flex;gap:10px;margin-bottom:20px}
.info-icon{width:30px;height:30px;border-radius:6px;background:var(--red-soft);display:flex;align-items:center;justify-content:center;flex:none}
.info-item h3{font-size:10px;font-weight:600;color:var(--ink);margin:2px 0 8px}
.info-item .main{font-size:10px;color:#333}
.info-item .sub{font-size:8.5px;color:#444;margin-top:5px}
.form-card{position:absolute;left:496px;top:59px;width:443px;height:456px;border:1px solid var(--line);border-radius:6px;background:#f7f7f7;padding:22px 20px}
.form-card h2{font-size:15px;font-weight:600;color:var(--ink);margin-bottom:17px}
.row{display:flex;gap:10px;margin-bottom:14px}
.field{flex:1}
.field label{display:block;font-size:8.5px;font-weight:600;color:var(--ink);margin-bottom:5px}
.field label i{color:var(--red);font-style:normal}
.input{height:26px;border:1px solid #d8d8d8;background:#fff;border-radius:3px;font-size:9.5px;color:#444;padding:0 10px;display:flex;align-items:center;justify-content:space-between}
.textarea{height:86px;align-items:flex-start;padding-top:8px}
.note{height:41px;margin-top:16px;border:1px solid #dedede;background:#ececec;border-radius:3px;font-size:7px;line-height:1.5;color:#444;padding:10px 10px}
.note span{color:var(--red)}
.form-card .btn{width:100%;height:29px;font-size:10px;margin-top:15px}

/* faq */
.faq{height:789px;background:var(--light);padding-top:58px}
.faq h2{text-align:center;font-size:23px;font-weight:700;color:var(--ink)}
.faq .lead{text-align:center;font-size:10px;color:#444;margin-top:10px}
.faq-list{width:519px;margin:30px auto 0}
.faq-item{height:85px;background:#fff;border:1px solid var(--line);border-radius:4px;padding:17px 15px 0;margin-bottom:16px}
.faq-item h3{font-size:10px;font-weight:600;color:var(--ink)}
.faq-item p{font-size:9.5px;line-height:1.7;color:#3a3a3a;margin-top:8px}

/* phone cta */
.call{height:220px;background:var(--dark);color:#fff;text-align:center;padding-top:55px}
.call h2{font-size:23px;font-weight:700}
.call p{font-size:11px;color:#ddd;margin-top:14px}
.call .btn{height:29px;padding:0 20px;font-size:10.5px;margin-top:20px}

/* newsletter */
.news{height:273px;background:linear-gradient(90deg,#1c1c1c,#3a3a3a);color:#fff;position:relative}
.news-left{position:absolute;left:340px;top:70px;width:210px}
.news-tag{display:flex;align-items:center;gap:9px;font-size:8.5px;font-weight:600;color:var(--red);letter-spacing:.04em}
.news-tag .ic{width:29px;height:29px;border-radius:6px;background:#4a1a17;display:flex;align-items:center;justify-content:center}
.news-left h2{font-size:22px;font-weight:700;margin-top:14px}
.news-left p{font-size:11px;line-height:1.6;color:#e0e0e0;margin-top:12px}
.news-form{position:absolute;left:565px;top:110px}
.news-row{display:flex;gap:8px}
.email-in{width:181px;height:37px;border:1px solid #777;background:#474747;border-radius:5px;font-size:10px;color:#b8b8b8;display:flex;align-items:center;padding-left:13px}
.news-row .btn{width:105px;height:37px;border-radius:5px;font-size:10.5px;gap:6px}
.news-form small{display:block;font-size:7px;color:#bbb;margin-top:8px}

/* footer */
.footer{height:235px;background:var(--dark);color:#ddd;position:relative;border-top:1px solid #3a3a3a}
.f-col{position:absolute;top:40px;font-size:8.5px}
.f-col h4{font-size:10px;font-weight:600;color:#fff;margin-bottom:12px}
.f-col li{list-style:none;margin-bottom:8px}
.f-col li.ci{display:flex;align-items:center;gap:7px}
.f-brand{left:220px;top:43px}
.f-brand p{width:180px;font-size:8.5px;line-height:1.5;margin-top:12px}
.f-rule{position:absolute;left:220px;width:759px;top:161px;border-top:1px solid #333}
.cookie{position:absolute;left:0;right:0;bottom:0;height:62px;background:#0c0c0c;color:#ddd}
.cookie h5{position:absolute;left:240px;top:17px;font-size:9.5px;font-weight:600;color:#fff}
.cookie p{position:absolute;left:240px;top:38px;font-size:7.8px}
.cookie p span{color:var(--red)}
.cookie .actions{position:absolute;left:820px;top:20px;display:flex;gap:7px;align-items:center}
.ghost{height:22px;width:49px;border:1px solid #bbb;border-radius:3px;font-size:8.5px;font-weight:600;color:#fff;display:flex;align-items:center;justify-content:center}
.cookie .btn{height:22px;width:60px;font-size:8.5px}
.x{margin-left:12px}
</style>
</head>
<body>

<header class="hero">
  <nav class="nav">
    <div class="brand"><span class="brand-mark">G</span>GLANZHALLEN</div>
    <div class="nav-links"><span>Home</span><span>About</span><span>Services</span><span>Products</span><span class="btn">Contact</span></div>
  </nav>
  <div class="hero-body">
    <span class="tag">LET'S CONNECT</span>
    <h1>Get in Touch</h1>
    <p>Ready to discuss your project? Contact our team for a free consultation and customized proposal.</p>
  </div>
</header>

<section class="contact">
  <div class="info">
    <h2>Contact Information</h2>
    <div class="info-item">
      <div class="info-icon"><svg width="14" height="14" viewBox="0 0 24 24" fill="none" stroke="#ee2416" stroke-width="2" stroke-linecap="round" stroke-linejoin="round"><path d="M22 16.9v3a2 2 0 0 1-2.2 2 19.8 19.8 0 0 1-8.6-3.1 19.5 19.5 0 0 1-6-6A19.8 19.8 0 0 1 2.1 4.2 2 2 0 0 1 4.1 2h3a2 2 0 0 1 2 1.7c.1 1 .4 1.9.7 2.8a2 2 0 0 1-.5 2.1L8 9.8a16 16 0 0 0 6 6l1.3-1.3a2 2 0 0 1 2.1-.4c.9.3 1.8.6 2.8.7a2 2 0 0 1 1.7 2z"/></svg></div>
      <div><h3>Telephone</h3><div class="main">+41 44 555 01 50</div><div class="sub">Mon-Fri: 8:00 - 17:00 CET</div></div>
    </div>
    <div class="info-item">
      <div class="info-icon"><svg width="14" height="14" viewBox="0 0 24 24" fill="none" stroke="#ee2416" stroke-width="2" stroke-linecap="round" stroke-linejoin="round"><rect x="2" y="4" width="20" height="16" rx="2"/><path d="m22 7-10 6L2 7"/></svg></div>
      <div><h3>Email</h3><div class="main">info@glanzhallenwerk.ch</div><div class="sub">Rapid response to inquiries</div></div>
    </div>
    <div class="info-item">
      <div class="info-icon"><svg width="14" height="14" viewBox="0 0 24 24" fill="none" stroke="#ee2416" stroke-width="2" stroke-linecap="round" stroke-linejoin="round"><path d="M20 10c0 6-8 12-8 12s-8-6-8-12a8 8 0 0 1 16 0z"/><circle cx="12" cy="10" r="3"/></svg></div>
      <div><h3>Location</h3><div class="main">Glanzhallen AG</div><div class="sub">Switzerland</div></div>
    </div>
    <div class="info-item">
      <div class="info-icon"><svg width="14" height="14" viewBox="0 0 24 24" fill="none" stroke="#ee2416" stroke-width="2" stroke-linecap="round" stroke-linejoin="round"><circle cx="12" cy="12" r="10"/><path d="M12 6v6l4 2"/></svg></div>
      <div><h3>Hours</h3><div class="sub" style="margin-top:0">Monday - Friday</div><div class="sub">8:00 AM - 5:00 PM CET</div></div>
    </div>
  </div>

  <div class="form-card">
    <h2>Send us a Message</h2>
    <div class="row">
      <div class="field"><label>Full Name <i>*</i></label><div class="input">Your name</div></div>
      <div class="field"><label>Email <i>*</i></label><div class="input">your@email.com</div></div>
    </div>
    <div class="row">
      <div class="field"><label>Phone Number</label><div class="input">+41 44 XXX XX XX</div></div>
      <div class="field"><label>Company Name</label><div class="input">Your company</div></div>
    </div>
    <div class="row">
      <div class="field"><label>Area of Interest <i>*</i></label><div class="input" style="color:#222">Select an option...<svg width="8" height="8" viewBox="0 0 24 24" fill="none" stroke="#222" stroke-width="3"><path d="m6 9 6 6 6-6"/></svg></div></div>
    </div>
    <div class="row" style="margin-bottom:0">
      <div class="field"><label>Message <i>*</i></label><div class="input textarea">Tell us about your project, requirements, and timeline...</div></div>
    </div>
    <div class="note">We respect your privacy. Your information will only be used to respond to your inquiry and will not be shared with third parties. See our <span>Privacy Policy</span> for more details.</div>
    <div class="btn">Send Inquiry</div>
  </div>
</section>

<section class="faq">
  <h2>Frequently Asked Questions</h2>
  <p class="lead">Quick answers to common inquiries</p>
  <div class="faq-list">
    <div class="faq-item"><h3>What is the typical timeline for a custom system?</h3><p>Project timelines vary based on complexity, but most systems take 8-12 weeks from order to installation. We provide detailed schedules during the planning phase.</p></div>
    <div class="faq-item"><h3>Do you offer financing or leasing options?</h3><p>Yes, we work with various financing partners to make system investments more manageable. Contact our team to discuss options suitable for your budget.</p></div>
    <div class="faq-item"><h3>What warranty coverage is included?</h3><p>We offer up to 6 years of warranty on select products, covering manufacturing defects and parts. Extended warranty options are also available.</p></div>
    <div class="faq-item"><h3>Can you retrofit our existing equipment?</h3><p>Absolutely. We specialize in efficiency retrofits and upgrades for aging systems. We'll evaluate your current setup and recommend cost-effective improvements.</p></div>
    <div class="faq-item"><h3>How often does maintenance need to occur?</h3><p>Maintenance frequency depends on usage, but most systems require quarterly filter changes and annual professional service. We'll establish a schedule during commissioning.</p></div>
    <div class="faq-item"><h3>Are your systems environmentally compliant?</h3><p>Yes, all systems meet or exceed Swiss industrial standards and EU environmental regulations. We use efficient filtration and include heat recovery options.</p></div>
  </div>
</section>

<section class="call">
  <h2>Prefer to Talk by Phone?</h2>
  <p>Our team is ready to discuss your project and answer any technical questions.</p>
  <span class="btn">Call +41 44 555 01 50</span>
</section>

<section class="news">
  <div class="news-left">
    <div class="news-tag"><span class="ic"><svg width="14" height="14" viewBox="0 0 24 24" fill="none" stroke="#ee2416" stroke-width="2" stroke-linecap="round" stroke-linejoin="round"><rect x="2" y="4" width="20" height="16" rx="2"/><path d="m22 7-10 6L2 7"/></svg></span>NEWSLETTER</div>
    <h2>Stay Informed</h2>
    <p>Get industry insights, product updates, and exclusive technical information delivered to your inbox.</p>
  </div>
  <div class="news-form">
    <div class="news-row">
      <div class="email-in">Your email address</div>
      <span class="btn">Subscribe <svg width="10" height="10" viewBox="0 0 24 24" fill="none" stroke="#fff" stroke-width="2.5" stroke-linecap="round"><path d="M5 12h14M13 6l6 6-6 6"/></svg></span>
    </div>
    <small>We respect your privacy. Unsubscribe at any time.</small>
  </div>
</section>

<footer class="footer">
  <div class="f-col f-brand">
    <div class="brand"><span class="brand-mark" style="width:25px;height:25px">G</span>GLANZHALLEN</div>
    <p>Swiss engineering excellence in industrial air technology and custom fabrication since 1967.</p>
  </div>
  <div class="f-col" style="left:415px"><h4>Company</h4><ul><li>About Us</li><li>Services</li><li>Products</li><li>Contact</li></ul></div>
  <div class="f-col" style="left:610px"><h4>Solutions</h4><ul><li>Spray Booths</li><li>Extraction Systems</li><li>Air Filtration</li><li>Service &amp; Support</li></ul></div>
  <div class="f-col" style="left:805px"><h4>Contact</h4><ul>
    <li class="ci"><svg width="9" height="9" viewBox="0 0 24 24" fill="none" stroke="#ddd" stroke-width="2"><path d="M22 16.9v3a2 2 0 0 1-2.2 2 19.8 19.8 0 0 1-8.6-3.1 19.5 19.5 0 0 1-6-6A19.8 19.8 0 0 1 2.1 4.2 2 2 0 0 1 4.1 2h3a2 2 0 0 1 2 1.7c.1 1 .4 1.9.7 2.8a2 2 0 0 1-.5 2.1L8 9.8a16 16 0 0 0 6 6l1.3-1.3a2 2 0 0 1 2.1-.4c.9.3 1.8.6 2.8.7a2 2 0 0 1 1.7 2z"/></svg>+41 44 555 01 50</li>
    <li class="ci"><svg width="9" height="9" viewBox="0 0 24 24" fill="none" stroke="#ddd" stroke-width="2"><rect x="2" y="4" width="20" height="16" rx="2"/><path d="m22 7-10 6L2 7"/></svg>info@glanzhallenwerk.ch</li>
    <li class="ci"><svg width="9" height="9" viewBox="0 0 24 24" fill="none" stroke="#ddd" stroke-width="2"><path d="M20 10c0 6-8 12-8 12s-8-6-8-12a8 8 0 0 1 16 0z"/><circle cx="12" cy="10" r="3"/></svg>Switzerland</li>
  </ul></div>
  <div class="f-rule"></div>
  <div class="cookie">
    <h5>Cookie Consent</h5>
    <p>We use cookies to enhance your experience and analyze site traffic. By continuing to use this site, you agree to our use of cookies. <span>Learn more</span></p>
    <div class="actions">
      <span class="ghost">Reject</span><span class="btn">Accept</span>
      <svg class="x" width="10" height="10" viewBox="0 0 24 24" fill="none" stroke="#fff" stroke-width="2.5" stroke-linecap="round"><path d="M5 5l14 14M19 5 5 19"/></svg>
    </div>
  </div>
</footer>

</body>
</html>
```